Wool Product Label / Yarn Band

Looking to update the packaging on our wool products. This includes a design for a paper band to place around braided wool or yarn, and a design for a sticker to place on the outside of tissue paper wrapping. Open to updating or modifying the logo, which does not fit well on a round sticker, but the sticker could also be something wool related (like a sheep or drop spindle) that does not include the logo.
Target Market(s)
Wool crafters (knitters / spinners / felters). Mainly women, aged 30-70
Industry/Entity Type
Textile
Colors
Designer to choose colors to be used in the design.
Requirements
Must have
- Band needs to include, brand name, logo, url (fernloomstead.com), dyelot number, as well as the fiber content (ex: Merino Wool) and weight of the fiber (ex: 4oz).
Nice to have
- Band would ideally be easily customized because the weight and fiber content is variable and will be printed specifically for each product, Variable information can be on a sticker or printed directly on a band that can be printed on a standard printer. Attached is a photo of the current band and it's application.

```html
<!DOCTYPE html>
<html lang="en">
<head>
<meta charset="utf-8">
<title>Fernloomstead Yarn Band</title>
<link rel="stylesheet" href="https://fonts.googleapis.com/css2?family=Lato:wght@400;700&family=Roboto+Condensed:wght@400;700&display=swap">
<style>
  :root {
    --page: #f2f2f2;
    --ribbon-fill: #ffffff;
    --frame-dark: #4a4a4a;
    --brand-green: #7cc142;
    --text-gray: #555555;
    --tag-dark: #4d4d4f;
    --tag-text: #ffffff;
    --knit-yellow: #f6ec9a;
    --knit-green: #c9e4a6;
    --knit-blue: #b9e1ea;
    --knit-pink: #f5d2d6;
  }
  * { margin: 0; padding: 0; box-sizing: border-box; }
  html, body { width: 898px; height: 1200px; overflow: hidden; }
  body {
    background: var(--page);
    display: flex;
    align-items: center;
    justify-content: center;
  }
  .yarn-band {
    width: 840px;
    height: 216px;
    box-shadow: 0 6px 14px rgba(0,0,0,0.25);
  }
  .yarn-band svg { display: block; width: 100%; height: 100%; }
  .brand-name {
    font-family: "Roboto Condensed", sans-serif;
    font-weight: 700;
    font-size: 78px;
    fill: var(--brand-green);
  }
  .tagline {
    font-family: "Roboto Condensed", sans-serif;
    font-weight: 400;
    font-size: 28px;
    fill: var(--text-gray);
  }
  .side-info {
    font-family: "Lato", sans-serif;
    font-size: 22px;
    fill: var(--text-gray);
  }
  .tag-info {
    font-family: "Lato", sans-serif;
    font-size: 22px;
    fill: var(--tag-text);
  }
</style>
</head>
<body>
  <div class="yarn-band">
    <svg viewBox="0 0 1340 345" xmlns="http://www.w3.org/2000/svg">
      <defs>
        <linearGradient id="knitTones" x1="0" y1="0" x2="1" y2="1">
          <stop offset="0" stop-color="var(--knit-yellow)"/>
          <stop offset="0.3" stop-color="var(--knit-pink)"/>
          <stop offset="0.55" stop-color="var(--knit-yellow)"/>
          <stop offset="0.8" stop-color="var(--knit-blue)"/>
          <stop offset="1" stop-color="var(--knit-green)"/>
        </linearGradient>
        <linearGradient id="frameTone" x1="0" y1="0" x2="1" y2="0">
          <stop offset="0" stop-color="#a7b92c"/>
          <stop offset="0.5" stop-color="#5aa43a"/>
          <stop offset="1" stop-color="#1f5f80"/>
        </linearGradient>
      </defs>

      <rect class="knit-background" width="1340" height="345" fill="url(#knitTones)" role="img" aria-label="Pastel knit stitch pattern in yellow, pink, green and blue"/>

      <path class="ribbon-frame" d="M15,90 L420,90 C470,90 500,5 670,5 C840,5 870,90 920,90 L1325,90 L1268,175 L1325,260 L920,260 C870,260 840,340 670,340 C500,340 470,260 420,260 L15,260 L72,175 Z"
            fill="var(--ribbon-fill)" stroke="var(--frame-dark)" stroke-width="14" stroke-linejoin="miter"/>
      <path class="ribbon-accent" d="M15,90 L420,90 C470,90 500,5 670,5 C840,5 870,90 920,90 L1325,90 L1268,175 L1325,260 L920,260 C870,260 840,340 670,340 C500,340 470,260 420,260 L15,260 L72,175 Z"
            fill="none" stroke="url(#frameTone)" stroke-width="6" transform="translate(670 172.5) scale(0.985 0.955) translate(-670 -172.5)"/>

      <text class="brand-name" x="670" y="148" text-anchor="middle">fernloomstead</text>
      <text class="tagline" x="715" y="205" text-anchor="middle">hand painted yarn &amp; fibers</text>

      <text class="side-info dyelot" x="115" y="183">S/N: MER/SILK-BLEND1</text>
      <text class="side-info website" x="1108" y="183" text-anchor="middle">www.fernloomstead.com</text>

      <path class="fiber-tag" d="M475,228 L840,228 L815,262 L740,262 L720,300 L620,300 L600,262 L500,262 Z" fill="var(--tag-dark)"/>
      <text class="tag-info fiber-content" x="670" y="254" text-anchor="middle">85% Merino Wool | 15% Silk</text>
      <text class="tag-info weight" x="670" y="290" text-anchor="middle">Qty: 4oz</text>
    </svg>
  </div>
</body>
</html>
```